Brightway Limousines Company Website

we need a website designed for a national limousine company with global capabilities (meaning they can service clients throughout the US and the world)

They service mostly corporate/business travelers, and groups and meetings, with a small portion of their business devoted to retail clients (special events and personal travel)

The overall look should be corporate, and we prefer a responsive design. We will need a home page, a fleet page (examples can be seen here: https://www.brqcarriage.com/fleet
http://www.pellowaychauffeurs.com/our-fleet) and one interior page

Copy will be lorem epsum for now

We have no logo yet but can put a placeholder logo

Industry/Entity Type

It Company

```html
<!DOCTYPE html>
<html lang="en">
<head>
<meta charset="utf-8">
<title>Brightway Limousines</title>
<link href="https://fonts.googleapis.com/css2?family=Oswald:wght@300;400;600&family=Lato:wght@400;700&display=swap" rel="stylesheet">
<style>
:root{
  --ink:#231f1e;
  --blue-deep:#0d2f7e;
  --blue-mid:#1156a8;
  --blue-bright:#1a6fc4;
  --navy-text:#0f2a6b;
  --white:#ffffff;
  --band:#e4e5e8;
  --btn:#e9eaec;
}
*{box-sizing:border-box;margin:0;padding:0}
html,body{width:1163px;height:1200px;overflow:hidden}
body{position:relative;font-family:"Lato",sans-serif;color:var(--white);
  background:radial-gradient(ellipse 70% 50% at 50% 45%,#1763b5 0%,#0f4596 45%,var(--blue-deep) 100%)}
.abs{position:absolute}
.topbar{left:0;top:0;width:1163px;height:78px;background:var(--ink);border-top:5px solid var(--blue-mid);border-bottom:1px solid var(--blue-bright)}
.brand{display:flex;align-items:center;gap:8px;font-family:"Lato",sans-serif;font-weight:400;font-size:17px;color:var(--white);white-space:nowrap}
.brand .dot{width:10px;height:10px;border-radius:50%;background:var(--white)}
.header-brand{left:176px;top:38px}
.phone{right:178px;top:18px;text-align:right}
.phone .main{font-size:25px;line-height:1.1}
.phone .intl{font-size:14px}
.hero{left:0;top:78px;width:1163px;height:322px;background:linear-gradient(100deg,#3a3a2a 0%,#6c6f6a 18%,#c9ccd0 38%,#8d9096 58%,#2a2a2c 72%,#a9adb3 88%,#cfd2d6 100%)}
.arrow{top:206px}
.form{left:782px;top:78px;width:203px;height:256px;background:var(--blue-bright);padding:11px 15px}
.form label{display:block;font-family:"Oswald",sans-serif;font-weight:300;font-size:21px;line-height:1;margin-bottom:6px}
.form .field{height:22px;background:var(--white);border:1px solid #9cb8d8;margin-bottom:8px}
.form .reserve{margin-top:14px;height:50px;background:var(--btn);color:var(--blue-bright);font-family:"Oswald",sans-serif;font-weight:600;font-size:18px;display:flex;align-items:center;justify-content:center;box-shadow:0 2px 3px rgba(0,0,0,.3)}
.nav{left:0;top:400px;width:1163px;height:51px;background:linear-gradient(#f1f2f4,#d9dadd);display:flex;justify-content:center;align-items:center;gap:8px;font-family:"Oswald",sans-serif;font-weight:300;font-size:19px;color:var(--navy-text)}
.nav .current{font-weight:600;text-decoration:underline;text-underline-offset:4px}
.card{top:480px;height:238px;background:rgba(12,50,130,.55);border:1px solid rgba(10,30,90,.6);text-align:center}
.card .photo{margin:12px auto 0;height:84px;border:3px solid var(--blue-bright)}
.card h2{font-family:"Oswald",sans-serif;font-weight:300;font-size:30px;line-height:1;margin:10px 0 6px}
.card p{font-size:9.5px;line-height:12.6px;width:180px;margin:0 auto}
.btn{width:65px;height:24px;background:var(--btn);color:var(--blue-bright);font-family:"Oswald",sans-serif;font-weight:600;font-size:11px;display:flex;align-items:center;justify-content:center;border:1px solid #aab}
.card .btn{margin:10px auto 0}
.section-title{top:754px;font-family:"Oswald",sans-serif;font-weight:300;font-size:31px}
.testimonial{left:177px;width:245px;height:62px;display:flex;gap:8px;font-size:9.5px;line-height:12.6px;padding-left:2px;border-bottom:1px dotted rgba(255,255,255,.8)}
.testimonial p{width:210px}
.testimonial svg{flex:none;margin-top:2px}
.about-photo{left:452px;top:807px;width:257px;height:116px;background:linear-gradient(120deg,#7b8590,#d9dde0 45%,#f1f1f1 60%,#6f747a);border:3px solid #1650a0}
.about-text{left:452px;top:935px;width:257px;font-size:9.5px;line-height:12.8px}
.services{left:740px;top:800px;width:225px;list-style:none;font-size:14px;line-height:22.4px}
.services li{position:relative;padding-left:14px}
.services li::before{content:"";position:absolute;left:2px;top:9px;width:5px;height:5px;border-radius:50%;background:var(--white)}
.rule{left:178px;top:1098px;width:807px;border-top:2px dotted rgba(255,255,255,.8)}
.footer-brand{left:176px;top:1138px}
.copy{left:358px;top:1141px;font-size:10px;letter-spacing:1px}
.social{left:861px;top:1135px;display:flex;gap:9px}
.social span{width:18px;height:18px;border-radius:50%;background:#e6e8ec}
</style>
</head>
<body>
<header class="abs topbar"></header>
<div class="abs brand header-brand"><span class="dot"></span><span>Brightway Limousines</span></div>
<div class="abs phone"><div class="main">Call: 000 000 0000</div><div class="intl">International +1 (000) 000-0000</div></div>

<div class="abs hero" role="img" aria-label="Chauffeur in a grey suit standing beside a silver sedan and a white stretch limousine"></div>
<svg class="abs arrow" style="left:141px" width="18" height="34" viewBox="0 0 18 34"><path d="M15 2 3 17l12 15" fill="none" stroke="#1a6fc4" stroke-width="4"/></svg>
<svg class="abs arrow" style="left:1007px" width="18" height="34" viewBox="0 0 18 34"><path d="M3 2l12 15L3 32" fill="none" stroke="#1a6fc4" stroke-width="4"/></svg>

<form class="abs form">
  <label>NAME</label><div class="field"></div>
  <label>EMAIL</label><div class="field"></div>
  <label>PHONE NUMBER</label><div class="field"></div>
  <div class="reserve">MAKE A RESERVATION</div>
</form>

<nav class="abs nav">
  <span class="current">HOME</span><span>-</span><span>WHO WE ARE</span><span>-</span><span>OUR FLEET</span><span>-</span><span>CUSTOM PACKAGES</span><span>-</span><span>TESTIMONIALS</span><span>-</span><span>BOOK YOUR RIDE</span>
</nav>

<article class="abs card" style="left:177px;width:245px">
  <div class="photo" role="img" aria-label="Gloved hand opening a car door" style="width:188px;background:linear-gradient(120deg,#3e3e40,#bfc3c8 55%,#8a8e94)"></div>
  <h2>CORPORATE</h2>
  <p>Lorem Ipsum is simply dummy text of the printing and typesetting industry. Lorem Ipsum has been the industry's standard dummy text ever since the 1500s,</p>
  <div class="btn">MORE</div>
</article>
<article class="abs card" style="left:452px;width:258px">
  <div class="photo" role="img" aria-label="Chauffeur in cap at the wheel of a car" style="width:202px;background:linear-gradient(120deg,#2b2b2e,#9ea3aa 50%,#dfe3e6)"></div>
  <h2>BUSINESS</h2>
  <p>Lorem Ipsum is simply dummy text of the printing and typesetting industry. Lorem Ipsum has been the industry's standard dummy text ever since the 1500s,</p>
  <div class="btn">MORE</div>
</article>
<article class="abs card" style="left:740px;width:245px">
  <div class="photo" role="img" aria-label="Bride with a yellow bouquet in a limousine" style="width:190px;background:linear-gradient(120deg,#d8c94a,#6b5a3a 45%,#e8e4e0)"></div>
  <h2>PROM</h2>
  <p>Lorem Ipsum is simply dummy text of the printing and typesetting industry. Lorem Ipsum has been the industry's standard dummy text ever since the 1500s,</p>
  <div class="btn">MORE</div>
</article>

<h2 class="abs section-title" style="left:176px">TESTIMONIALS</h2>
<h2 class="abs section-title" style="left:452px">WHO WE ARE</h2>
<h2 class="abs section-title" style="left:740px">OUR SERVICES</h2>

<div class="abs testimonial" style="top:803px"><svg width="18" height="18" viewBox="0 0 18 18"><circle cx="9" cy="9" r="8" fill="none" stroke="#fff" stroke-width="1.6"/><path d="M5 9l3 3 5-6" fill="none" stroke="#fff" stroke-width="1.6"/></svg><p>Lorem Ipsum is simply dummy text of the printing and typesetting industry. Lorem Ipsum is simply dummy text of the printing and typesetting industry.</p></div>
<div class="abs testimonial" style="top:876px"><svg width="18" height="18" viewBox="0 0 18 18"><circle cx="9" cy="9" r="8" fill="none" stroke="#fff" stroke-width="1.6"/><path d="M5 9l3 3 5-6" fill="none" stroke="#fff" stroke-width="1.6"/></svg><p>Lorem Ipsum is simply dummy text of the printing and typesetting industry. Lorem Ipsum is simply dummy text of the printing and typesetting industry.</p></div>
<div class="abs testimonial" style="top:949px;border-bottom:none"><svg width="18" height="18" viewBox="0 0 18 18"><circle cx="9" cy="9" r="8" fill="none" stroke="#fff" stroke-width="1.6"/><path d="M5 9l3 3 5-6" fill="none" stroke="#fff" stroke-width="1.6"/></svg><p>Lorem Ipsum is simply dummy text of the printing and typesetting industry. Lorem Ipsum is simply dummy text of the printing and typesetting industry.</p></div>
<div class="abs btn" style="left:177px;top:1026px">MORE</div>

<div class="abs about-photo" role="img" aria-label="Woman in white standing beside a white luxury car in a city street"></div>
<p class="abs about-text">Lorem Ipsum is simply dummy text of the printing and typesetting industry. Lorem Ipsum has been the industry's standard dummy text ever since the 1500s, when an unknown printer took a galley of type and scrambled it to make a type specimen book.</p>
<div class="abs btn" style="left:453px;top:1026px">MORE</div>

<ul class="abs services">
  <li>Worldwide Services</li>
  <li>Airport Transfers</li>
  <li>Meetings, Groups and Special Events</li>
  <li>Corporate and Convention Shuttles</li>
  <li>Roadshows</li>
  <li>Jet Charters and Private Aviation</li>
  <li>Frequent Rider Program</li>
</ul>

<div class="abs rule"></div>
<footer>
  <div class="abs brand footer-brand"><span class="dot"></span><span>Brightway Limousines</span></div>
  <p class="abs copy">© 2014 | Privacy Policy</p>
  <div class="abs social"><span></span><span></span><span></span><span></span><span></span></div>
</footer>
</body>
</html>
```